New Landing page in Wordpress Design Project

Hi we have launched a new website www.velmorewindowdrapes.co.uk and although we are doing a PPC campaign and getting a good number of hits, we are not getting enquiries. I need the website to be adjusted to improve visitor retention and I am lead to believe if your landing page is poor that is the main reason. At the moment the home page is the landing page. I am happy to amend this or add a additional landing page. My own web guru will make the necessary changes. I want to portray a top quality looking site

Industry/Entity Type

Campaign

```html
<!DOCTYPE html>
<html lang="en">
<head>
<meta charset="utf-8">
<title>Velmore Window Drapes</title>
<link href="https://fonts.googleapis.com/css2?family=Source+Sans+3:wght@400;600&family=Lato:ital,wght@0,300;0,400;0,700;1,400&family=Open+Sans:wght@400;700&display=swap" rel="stylesheet">
<style>
  :root {
    --page-bg: #fbf4f8;
    --pink: #e776b0;
    --pink-dark: #de5fa2;
    --pink-line: #e58fbd;
    --teal: #1f7d78;
    --navy: #302d40;
    --sea: #4aa79a;
    --coral: #c35658;
    --badge: #f7f1dc;
    --text: #4a4a4a;
    --link-grey: #5b5450;
    --white: #ffffff;
  }
  * { box-sizing: border-box; margin: 0; padding: 0; }
  html, body { width: 1200px; height: 1040px; overflow: hidden; }
  body {
    position: relative;
    background: radial-gradient(ellipse at 75% 5%, #eadcf0 0%, rgba(251,244,248,0) 45%),
                radial-gradient(ellipse at 10% 12%, #f5e4ef 0%, rgba(251,244,248,0) 40%),
                var(--page-bg);
    font-family: "Source Sans 3", Arial, sans-serif;
    color: var(--text);
  }
  .brand {
    position: absolute; left: 46px; top: 22px;
    font-family: "Source Sans 3", Arial, sans-serif;
    font-weight: 600; font-size: 34px; color: var(--teal);
    letter-spacing: 0.5px; line-height: 1;
    display: flex; align-items: center; gap: 10px;
  }
  .brand-mark { width: 14px; height: 14px; background: var(--teal); display: inline-block; }
  .utility-nav {
    position: absolute; right: 47px; top: 34px;
    display: flex; align-items: center; font-size: 13px; color: var(--link-grey);
  }
  .utility-nav a { color: var(--link-grey); text-decoration: none; }
  .utility-nav .sep { margin: 0 10px; }
  .login {
    margin-left: 14px; display: flex; align-items: center; gap: 6px;
    background: #5a75a8; color: var(--white); font-weight: 600; font-size: 11px;
    height: 19px; padding: 0 6px 0 3px;
  }
  .login .sq { width: 13px; height: 13px; background: var(--white); opacity: .85; }
  .main-nav {
    position: absolute; left: 43px; top: 104px; width: 1118px; height: 76px;
    background: linear-gradient(#ea84b9, var(--pink-dark));
  }
  .main-nav::after {
    content: ""; position: absolute; inset: 9px 11px;
    border: 1px dashed rgba(255,255,255,.6); pointer-events: none;
  }
  .main-nav ul { list-style: none; display: flex; height: 100%; padding-left: 14px; }
  .main-nav li { height: 100%; display: flex; align-items: center; padding: 0 18px; color: var(--white); font-size: 16.5px; }
  .main-nav li.current { background: rgba(240,80,150,.55); }
  .hero {
    position: absolute; left: 43px; top: 180px; width: 1118px; height: 314px;
    background: linear-gradient(90deg, #6f5a4a 0%, #8b97ad 15%, #c6c8cc 30%, #3a2f3b 40%, #d8c8ad 55%, #cfbfa4 68%, #7e2a4a 80%, #a5899a 100%);
  }
  .promo-strip {
    position: absolute; left: 30px; top: 520px; width: 1140px; height: 122px; background: var(--white); opacity: .65;
  }
  .promo {
    position: absolute; top: 526px; height: 102px; width: 357px;
    display: flex; align-items: center; justify-content: center;
    color: var(--white); font-family: "Lato", sans-serif; font-size: 26px; letter-spacing: 1px;
  }
  .promo.offers { left: 44px; background: var(--navy); font-weight: 400; }
  .promo.offers .amp { font-family: Georgia, serif; font-style: italic; font-size: 24px; margin: 0 6px; }
  .promo.delivery { left: 424px; background: var(--sea); font-weight: 300; font-size: 28px; }
  .promo.delivery em { font-weight: 400; margin-right: 8px; }
  .promo.delivery sup { font-size: 11px; margin-left: 2px; }
  .promo.sale { left: 803px; background: var(--coral); justify-content: flex-start; padding-left: 47px; font-weight: 300; font-size: 29px; }
  .promo.sale b { font-weight: 700; margin-right: 8px; }
  .promo.sale svg { position: absolute; right: 5px; top: 4px; }
  .section-title {
    position: absolute; left: 54px; top: 658px; font-size: 24px; color: var(--pink); font-weight: 400;
  }
  .section-rule { position: absolute; left: 54px; top: 696px; width: 1101px; border-top: 1px dashed var(--pink-line); }
  .product { position: absolute; top: 715px; width: 190px; }
  .product .frame { width: 185px; height: 150px; border: 1px dashed var(--pink-line); padding: 6px; }
  .product .photo { width: 100%; height: 100%; }
  .product p {
    margin-top: 12px; font-family: "Open Sans", Verdana, sans-serif; font-size: 10.5px;
    line-height: 17px; letter-spacing: .5px; color: var(--text);
  }
  .product .more {
    display: block; margin-top: 4px; font-family: "Open Sans", Verdana, sans-serif;
    font-size: 11px; font-weight: 700; letter-spacing: 1px; color: #222; text-decoration: none;
  }
  .footer {
    position: absolute; left: 43px; top: 998px; width: 1115px; height: 42px; background: var(--navy);
    color: var(--white); font-size: 11.5px; display: flex; justify-content: space-between; align-items: center; padding: 0 12px;
  }
</style>
</head>
<body>
  <div class="brand"><span class="brand-mark"></span>Velmore Window Drapes</div>

  <nav class="utility-nav">
    <a href="#">HOME</a><span class="sep">|</span><a href="#">SITEMAP</a>
    <span class="login"><span class="sq"></span>Login</span>
  </nav>

  <nav class="main-nav">
    <ul>
      <li class="current">ABOUT US</li>
      <li>NEWS</li>
      <li>CURTAINS</li>
      <li>SCATTER CUSHIONS &amp; BED THROWS</li>
      <li>GALLERY</li>
      <li>CONTACT US</li>
      <li>TESTIMONIALS</li>
    </ul>
  </nav>

  <div class="hero" role="img" aria-label="Luxurious living room with draped blue-grey curtains, a tufted leather armchair and a plum velvet sofa"></div>

  <div class="promo-strip"></div>
  <div class="promo offers">DISCOUNTS<span class="amp">&amp;</span>OFFERS</div>
  <div class="promo delivery"><em>FREE</em>UK DELIVERY<sup>*</sup></div>
  <div class="promo sale"><b>SALE</b>NOW ON
    <svg width="94" height="94" viewBox="0 0 94 94" aria-hidden="true">
      <polygon fill="var(--badge)" points="47,0 52,8 59,2 62,11 70,7 71,16 80,14 79,23 88,24 84,32 93,36 87,42 94,47 87,52 93,58 84,62 88,70 79,71 80,80 71,78 70,87 62,83 59,92 52,86 47,94 42,86 35,92 32,83 24,87 23,78 14,80 15,71 6,70 10,62 1,58 7,52 0,47 7,42 1,36 10,32 6,24 15,23 14,14 23,16 24,7 32,11 35,2 42,8"/>
      <text x="47" y="53" text-anchor="middle" font-family="Georgia, serif" font-weight="700" font-size="15" fill="var(--coral)">SALE</text>
    </svg>
  </div>

  <h2 class="section-title">OUR PRODUCTS</h2>
  <div class="section-rule"></div>

  <div class="product" style="left:54px">
    <div class="frame"><div class="photo" role="img" aria-label="Patterned grey curtains beside black vases" style="background:linear-gradient(90deg,#555 0%,#8a8a88 40%,#d8d6cf 70%,#2b2b2b 100%)"></div></div>
    <p>Lorem ipsum dolor sit amet, conr adipiscing elit. Praeset mi tellus, egestas facilisis pulvinar non.</p>
    <a class="more" href="#">Read More</a>
  </div>
  <div class="product" style="left:285px">
    <div class="frame"><div class="photo" role="img" aria-label="Assorted decorative scatter cushions in yellow, teal and cream" style="background:linear-gradient(135deg,#3f5a5c 0%,#6a5a42 40%,#c6ae3a 65%,#2f2e2a 100%)"></div></div>
    <p>Lorem ipsum dolor sit amet, conr adipiscing elit. Praeset mi tellus, egestas facilisis pulvinar non.</p>
    <a class="more" href="#">Read More</a>
  </div>
  <div class="product" style="left:516px">
    <div class="frame"><div class="photo" role="img" aria-label="White sofa with colourful striped cushions in a bright room" style="background:linear-gradient(180deg,#e9e3d6 0%,#d6d4cc 50%,#f4f4f2 70%,#8f8a80 100%)"></div></div>
    <p>Lorem ipsum dolor sit amet, conr adipiscing elit. Praeset mi tellus, egestas facilisis pulvinar non.</p>
    <a class="more" href="#">Read More</a>
  </div>
  <div class="product" style="left:747px">
    <div class="frame"><div class="photo" role="img" aria-label="Dark armchair with a yellow striped cushion" style="background:linear-gradient(135deg,#3a3f35 0%,#26262a 45%,#8f8a3a 65%,#1f1f22 100%)"></div></div>
    <p>Lorem ipsum dolor sit amet, conr adipiscing elit. Praeset mi tellus, egestas facilisis pulvinar non.</p>
    <a class="more" href="#">Read More</a>
  </div>
  <div class="product" style="left:969px">
    <div class="frame"><div class="photo" role="img" aria-label="Plum satin cushions with beaded trim on a dark rug" style="background:linear-gradient(135deg,#2a2224 0%,#4a3a42 45%,#6b5560 70%,#b39c7e 100%)"></div></div>
    <p>Lorem ipsum dolor sit amet, conr adipiscing elit. Praeset mi tellus, egestas facilisis pulvinar non.</p>
    <a class="more" href="#">Read More</a>
  </div>

  <footer class="footer">
    <span>Home | Sitemap | Terms &amp; Condition</span>
    <span>© 2013 Copyrights Velmore Window Drapes All Rights Reserved</span>
  </footer>
</body>
</html>
```